Tri-fold Brochure Design for Law Firm

I need a tri-fold brochure to give to prospective clients.
I have attached a Photoshop design file of a tri-fold brochure. The content (copy) is good, however, he brochure itself looks very amateurish.
I want a professional, sophisticated looking brochure.
The law firm specializes in commercial debt collection.
The law firm is located in New York City.
Our target market is business owners, doctors, lawyers, collection agencies and accountants.
Visit my website which is being designed at www.dornvek.com. I like the font used for the name of my company and the rich blue color used.

Target Market(s)

Business Owners, Doctors, Law Firms and Accountants

Industry/Entity Type

Law Firm

Font styles to use
Serif

Requirements
Must have
• Professional quality graphic work. Attention to details.
• PHOTOGRAPHS ONLY, NO CLIP-ART.
• DARK COLORS - NAVY BLUE, HUNTER GREEN, BLACK, GRAY & WHITE
Nice to have
• I want it to look smart, modern and sophisticated.
• Visit my website which is being designed at www.dornvek.com. I like the font used for the name of my company and the rich blue color used.
Should not have
• Bad artwork
• CLIP ART

```html
<!DOCTYPE html>
<html lang="en">
<head>
<meta charset="utf-8">
<title>Marcello Dornvek &amp; Company PLLC – Tri-fold Brochure</title>
<link rel="stylesheet" href="https://fonts.googleapis.com/css2?family=Marcellus&family=Didact+Gothic&family=Tinos:wght@400;700&family=Mulish:wght@700;800&display=swap">
<style>
  :root {
    --blue: #1f5cb8;
    --blue-deep: #184b9c;
    --grey: #b9bcc1;
    --grey-light: #d9dbde;
    --ink: #222428;
    --paper: #ffffff;
    --backdrop: #e6e7e9;
  }
  * { box-sizing: border-box; margin: 0; padding: 0; }
  html, body { width: 1200px; height: 960px; overflow: hidden; background: var(--backdrop); }
  body { position: relative; font-family: "Didact Gothic", sans-serif; color: var(--ink); }

  .sheet { position: absolute; left: 20px; width: 1160px; display: flex; background: var(--paper); box-shadow: 0 4px 14px rgba(0,0,0,.18); overflow: hidden; }
  .sheet--outside { top: 16px; height: 430px; }
  .sheet--inside { top: 462px; height: 482px; }
  .panel { position: relative; width: 386.67px; height: 100%; overflow: hidden; }

  /* ---------- outside: trusted partner ---------- */
  .panel--partner { background: var(--blue); color: #fff; padding: 22px 26px; }
  .partner__title { font-family: "Mulish", sans-serif; font-weight: 800; font-size: 22px; letter-spacing: .5px; margin-bottom: 10px; }
  .partner__text { font-size: 10.5px; line-height: 1.38; text-align: justify; }
  .partner__text + .partner__text { margin-top: 4px; }
  .partner__lead { font-weight: 700; font-size: 11px; margin-top: 6px; }
  .partner__list { list-style: none; font-size: 11px; line-height: 14.2px; margin-top: 3px; padding-left: 6px; }
  .partner__list li::before { content: "• "; }

  /* ---------- outside: contact ---------- */
  .panel--contact { background: var(--blue); }
  .contact__photo { position: absolute; left: 0; top: 0; width: 100%; height: 222px; background: linear-gradient(90deg, #c9c6c0 0%, #f4f2ee 18%, #d8d4cd 30%, #f7f6f3 45%, #cfcbc4 58%, #f3f1ed 72%, #c8c4bd 86%, #ebe8e3 100%); }
  .contact__card { position: absolute; left: 0; top: 26px; width: 100%; text-align: center; color: var(--blue); }
  .firm-name { font-family: "Marcellus", serif; line-height: 1.05; letter-spacing: 1px; }
  .contact__card .firm-name { font-size: 28px; }
  .firm-name small { font-size: .55em; }
  .contact__tag { font-size: 9px; margin: 4px 0 10px; }
  .contact__web { font-family: "Mulish", sans-serif; font-weight: 700; font-size: 13px; margin-bottom: 6px; }
  .contact__person { font-family: "Mulish", sans-serif; font-weight: 700; font-size: 13px; }
  .contact__line { font-size: 11px; line-height: 1.35; }
  .contact__notch { position: absolute; left: 50%; top: 194px; width: 58px; height: 58px; margin-left: -29px; border-radius: 50%; background: var(--blue); display: flex; align-items: center; justify-content: center; }
  .contact__offices { position: absolute; left: 0; top: 250px; width: 100%; text-align: center; color: #fff; }
  .office__head { font-family: "Mulish", sans-serif; font-weight: 800; font-size: 12.5px; letter-spacing: .4px; }
  .office__line { font-size: 10.5px; line-height: 1.35; }
  .office + .office { margin-top: 6px; }
  .contact__pill { position: absolute; left: 0; top: 362px; width: 312px; height: 54px; background: var(--grey-light); border-radius: 0 27px 27px 0; padding: 6px 0 0 78px; color: var(--blue); font-family: "Mulish", sans-serif; font-weight: 800; font-size: 11px; line-height: 1.3; }
  .contact__phone-icon { position: absolute; left: 8px; top: 2px; width: 50px; height: 50px; border-radius: 50%; background: var(--paper); display: flex; align-items: center; justify-content: center; }

  /* ---------- outside: cover ---------- */
  .cover__art { position: absolute; inset: 0; }
  .cover__title { position: absolute; left: 30px; top: 30px; color: #fff; }
  .cover__title .firm-name { font-size: 30px; }
  .cover__tag { font-family: "Mulish", sans-serif; font-weight: 800; font-size: 14px; margin-top: 6px; }
  .cover__phone { position: absolute; left: 0; bottom: 12px; width: 100%; text-align: center; color: #fff; font-family: "Mulish", sans-serif; font-weight: 800; font-size: 30px; }

  /* ---------- inside ---------- */
  .inside__photos { position: absolute; left: 0; top: 0; width: 773.34px; height: 120px; }
  .panel--inner { padding: 0 24px 14px; font-size: 9.8px; line-height: 1.3; }
  .panel--inner + .panel--inner { border-left: 1px solid #e3e4e6; }
  .panel--inner.has-photo { padding-top: 112px; }
  .panel--inner.no-photo { padding-top: 18px; }
  .section-head { display: flex; align-items: stretch; margin: 9px 0 5px; }
  .section-head::before { content: ""; width: 16px; background: var(--grey); }
  .section-head span { background: var(--blue); color: #fff; font-family: "Tinos", serif; font-size: 15px; letter-spacing: .4px; padding: 3px 10px 2px; }
  .copy { text-align: justify; }
  .copy + .copy { margin-top: 5px; }
  .copy em { font-style: italic; font-weight: 700; }
  .subhead { color: var(--blue); font-weight: 700; font-style: italic; font-size: 10.5px; margin-bottom: 3px; }
  .fee-list { list-style: none; color: var(--blue); margin: 4px 0 0 12px; }
  .fee-list li::before { content: "• "; }
</style>
</head>
<body>

<!-- OUTSIDE -->
<section class="sheet sheet--outside">
  <article class="panel panel--partner">
    <h2 class="partner__title">A TRUSTED PARTNER</h2>
    <p class="partner__text">We understand the business of debt collection. Our primary focus is to help our clients secure the payments they are owed. We work closely with both private clients and leading service professionals, such as attorneys and accountants, to provide added value to their clients through customized debt collection services.</p>
    <p class="partner__text">We value our relationships as trusted advisors.</p>
    <p class="partner__lead">We proudly serve:</p>
    <ul class="partner__list">
      <li>Law firms</li>
      <li>Accounting Firms</li>
      <li>Manufacturers</li>
      <li>Wholesalers and Distributors</li>
      <li>Collection Agencies</li>
      <li>Financial Service Companies</li>
      <li>Factors</li>
      <li>Doctors and Healthcare Professionals</li>
      <li>Carting Companies</li>
      <li>Oil Companies</li>
      <li>Freight Forwarders &amp; Custom Brokers</li>
      <li>Publishing and Advertising Companies</li>
      <li>Construction and Real Estate Firms</li>
    </ul>
  </article>

  <article class="panel panel--contact">
    <div class="contact__photo" role="img" aria-label="Photograph of white classical marble columns"></div>
    <div class="contact__card">
      <h2 class="firm-name">MARCELLO DORNVEK<br>&amp; COMPANY <small>PLLC</small></h2>
      <p class="contact__tag">Debt Collection Attorneys in New York State</p>
      <p class="contact__web">www.dornvek.com</p>
      <p class="contact__person">MARCELLO J. DORNVEK, ESQUIRE</p>
      <p class="contact__line">President</p>
      <p class="contact__line">mdornvek@dornvek.com</p>
      <p class="contact__line">(212) 555-0147 Cell</p>
    </div>
    <div class="contact__notch">
      <svg width="26" height="26" viewBox="0 0 24 24" fill="none" stroke="#fff" stroke-width="2" stroke-linejoin="round"><path d="M22 2 2 10l8 3 3 8z"/><path d="M22 2 10 13"/></svg>
    </div>
    <div class="contact__offices">
      <div class="office">
        <p class="office__head">WESTCHESTER COUNTY OFFICE</p>
        <p class="office__line">450 HARLOW AVENUE, SUITE 210<br>WHITE PLAINS, NEW YORK 10605<br>(Off Exit 4, on Harlow Parkway)</p>
      </div>
      <div class="office">
        <p class="office__head">MAILING ADDRESS</p>
        <p class="office__line">316 LEXINGTON ROW, SUITE 5120<br>NEW YORK, NEW YORK 10016</p>
      </div>
    </div>
    <div class="contact__pill">
      <span class="contact__phone-icon">
        <svg width="26" height="26" viewBox="0 0 24 24" fill="var(--blue)"><path d="M6.6 10.8a15.1 15.1 0 0 0 6.6 6.6l2.2-2.2a1 1 0 0 1 1-.25 11.4 11.4 0 0 0 3.6.57 1 1 0 0 1 1 1V20a1 1 0 0 1-1 1A17 17 0 0 1 3 4a1 1 0 0 1 1-1h3.5a1 1 0 0 1 1 1c0 1.25.2 2.45.57 3.57a1 1 0 0 1-.25 1z"/></svg>
      </span>
      TOLL FREE: (877) 555-0190<br>LOCAL: (212) 555-0162<br>FAX: (917) 555-0173
    </div>
  </article>

  <article class="panel panel--cover">
    <svg class="cover__art" viewBox="0 0 387 430" preserveAspectRatio="none" aria-hidden="true">
      <rect width="387" height="430" fill="var(--blue)"/>
      <polygon points="300,0 387,0 387,120" fill="var(--grey)"/>
      <polygon points="330,0 387,0 387,60" fill="var(--grey-light)"/>
    </svg>
    <svg class="cover__art" viewBox="0 0 387 430" preserveAspectRatio="none" role="img" aria-label="Photograph of the New York City skyline at sunrise">
      <defs>
        <linearGradient id="skyline" x1="0" y1="0" x2="0" y2="1">
          <stop offset="0" stop-color="#e9d9b4"/>
          <stop offset=".45" stop-color="#b98a4e"/>
          <stop offset="1" stop-color="#3c3024"/>
        </linearGradient>
      </defs>
      <polygon points="0,230 387,150 387,372 0,372" fill="url(#skyline)"/>
      <polygon points="0,230 150,199 0,300" fill="var(--blue)"/>
    </svg>
    <div class="cover__title">
      <h1 class="firm-name">MARCELLO DORNVEK<br>&amp; COMPANY <small>PLLC</small></h1>
      <p class="cover__tag">Debt Collection Attorneys</p>
    </div>
    <p class="cover__phone">(877) 555-0190</p>
  </article>
</section>

<!-- INSIDE -->
<section class="sheet sheet--inside">
  <svg class="inside__photos" viewBox="0 0 773 120" preserveAspectRatio="none">
    <defs>
      <linearGradient id="library" x1="0" y1="0" x2="1" y2="0">
        <stop offset="0" stop-color="#6e4a35"/><stop offset=".6" stop-color="#9a7a62"/><stop offset="1" stop-color="#3d5a86"/>
      </linearGradient>
      <linearGradient id="gavel" x1="0" y1="0" x2="1" y2="1">
        <stop offset="0" stop-color="#5a3420"/><stop offset=".5" stop-color="#8a5a36"/><stop offset="1" stop-color="#3a2418"/>
      </linearGradient>
    </defs>
    <rect x="0" y="0" width="300" height="120" fill="url(#library)" role="img" aria-label="Photograph of a lawyer in a suit before shelves of law books"/>
    <rect x="300" y="0" width="473" height="120" fill="url(#gavel)" role="img" aria-label="Photograph of scales of justice, law books and a gavel"/>
    <path d="M0 70 Q 250 150 773 40 L773 120 L0 120 Z" fill="#fff"/>
  </svg>

  <article class="panel panel--inner has-photo">
    <h3 class="section-head"><span>WHO WE ARE</span></h3>
    <p class="copy"><em>MARCELLO DORNVEK &amp; COMPANY, PLLC ("DORNVEK")</em> is a New York based law firm devoted to the collection of accounts receivable and business debts.</p>
    <h3 class="section-head"><span>WHAT WE DO</span></h3>
    <p class="copy">Within 24 to 72 hours of receiving a claim, we will verify the debt, investigate the Debtor, skip trace all known stakeholders and file a lawsuit with the intent of collecting the full amount due in the shortest time possible.</p>
    <p class="copy">We will use all legal means necessary to locate, identify, seize, or otherwise garnish a Debtor's assets and income, while always having an attorney available to speak directly with the Debtor to achieve an amicable resolution as quickly as possible.</p>
    <h3 class="section-head"><span>OUR MISSION</span></h3>
    <p class="copy">Our mission is to protect our clients' bottom line, while preserving their reputation.</p>
    <p class="copy">We recognize and appreciate that your Debtor was once a trusted customer and may be a source of future revenue.</p>
    <p class="copy">We treat all Debtors with respect, while aggressively seeking to collect all monies owed.</p>
  </article>

  <article class="panel panel--inner has-photo">
    <h3 class="section-head"><span>FLEXIBLE FEE STRUCTURE</span></h3>
    <p class="copy">We recognize that each claim is unique, therefore to better serve our clients we offer a variety of fee structures that meet the needs of our clients. Including:</p>
    <ul class="fee-list">
      <li>Contingency Fee</li>
      <li>Flat Fee</li>
      <li>Hourly fee</li>
      <li>Monthly or Annual Retainer</li>
      <li>Any combination of the above</li>
    </ul>
    <h3 class="section-head"><span>HANDLING MEDICAL RECEIVABLES</span></h3>
    <p class="copy">Medical receivables require a soft touch.</p>
    <p class="copy">Doctors and health organizations often write-off tens of thousands of dollars in unpaid deductibles and co-insurance which are rightfully due them out of fear that pursuing these debts will alienate, upset or offend their patients.</p>
    <p class="copy">We offer non-legal, HIPAA compliant collection methods which can effectively and consistently turn these otherwise uncollectible assets into real cash.</p>
    <p class="copy">Using a combination of letters and phone calls, our staff contacts patients in a professional and friendly manner to arrange for payments, as small as $15 per month, encouraging them to pay all monies owed.</p>
  </article>

  <article class="panel panel--inner no-photo">
    <h3 class="section-head"><span>CREDIT ADVISORY SERVICES</span></h3>
    <p class="subhead">How well do you really know your customers?</p>
    <p class="copy">As an added service to all of our clients, we will draft a customized credit application to be distributed to all of their customers.</p>
    <p class="copy">Working closely and alongside their salespeople, we will discretely review and verify the customers' information and investigate all known stakeholders in order to determine creditworthiness.</p>
    <p class="copy">As your credit advisor, we will then make a meaningful recommendation with regard to the amount and terms credit should be offered to specific customers.</p>
    <p class="copy">Once a credit determination is made, we can provide the client with a credit agreement detailing each parties' obligations. Using such agreements minimizes risk, while enhancing our clients' professional stature with their customers.</p>
    <h3 class="section-head"><span>KEEPING YOU IN COMPLIANCE</span></h3>
    <p class="copy">As your collection attorney and advisor, we will assure that your collection practices are in full compliance with all applicable Federal and State laws, including The Fair Debt Collection Practices Act (FDCPA) and The Health Insurance Portability and Accountability Act (HIPAA).</p>
    <h3 class="section-head"><span>STATE-OF-THE-ART TECHNOLOGY</span></h3>
    <p class="copy">Our firm prides itself on utilizing the state-of-the-art technology in law office management, telephony, cyber security, document production, and cloud storage.</p>
    <p class="copy">Our clients can be assured that their critical business data is stored in a safe, secure, and confidential environment, while allowing us to seamlessly handle a large and ever growing book of business in a timely manner.</p>
  </article>
</section>

</body>
</html>
```